Business Card

I need a business card that really pops for a potential customer or person who refers a personal injury lead. I want to highlight our office locations, but only address that needs to be on the card is my office's main address. I want a sleek, modern and minimalist design.

```html
<!DOCTYPE html>
<html lang="en">
<head>
<meta charset="UTF-8">
<title>Lakeshore Injury Counsel — Business Card</title>
<link href="https://fonts.googleapis.com/css2?family=Lato:wght@400;700&family=Poppins:wght@300;800&display=swap" rel="stylesheet">
<style>
  :root {
    --backdrop: #a8d8d5;
    --card-dark: #262626;
    --card-light: #ffffff;
    --ink: #1b1b1b;
    --ink-soft: #3a3a3a;
    --silver: #d4d4d4;
    --firm-grey: #4a4a4a;
  }
  * { margin: 0; padding: 0; box-sizing: border-box; }
  html, body {
    width: 1200px; height: 1200px; overflow: hidden;
    background: var(--backdrop);
  }
  .canvas { position: relative; width: 1200px; height: 1200px; }
  .card {
    position: absolute; left: 220px; width: 760px; height: 434px;
    box-shadow: 0 14px 30px rgba(0,0,0,0.18);
    overflow: hidden;
  }
  /* Front */
  .card--front { top: 140px; background: var(--card-light); }
  .front__panel {
    position: absolute; inset: 0 0 96px 0;
    background: var(--card-dark);
    display: flex; align-items: center; justify-content: center;
  }
  .firm-name {
    font-family: "Lato", sans-serif; font-weight: 700;
    letter-spacing: 0; line-height: 1.2; white-space: nowrap;
  }
  .firm-name--front { color: var(--silver); font-size: 40px; }
  .front__band {
    position: absolute; left: 0; right: 0; bottom: 0; height: 96px;
    display: flex; align-items: center; justify-content: center; gap: 12px;
    font-family: "Lato", sans-serif; font-weight: 700; font-size: 21px; color: var(--ink);
  }
  .icon { width: 20px; height: 20px; fill: var(--ink); flex: none; }
  /* Back */
  .card--back { top: 626px; background: var(--card-light); }
  .person { position: absolute; left: 420px; top: 62px; }
  .person__name {
    display: flex; align-items: center; gap: 10px;
    font-family: "Poppins", sans-serif; font-size: 38px; line-height: 1; color: var(--ink);
  }
  .person__first { font-weight: 800; }
  .person__last { font-weight: 300; }
  .person__role {
    margin: 8px 0 0 32px;
    font-family: "Poppins", sans-serif; font-weight: 300; font-size: 19px;
    letter-spacing: 0.04em; color: var(--ink-soft);
  }
  .contacts {
    position: absolute; left: 452px; top: 200px; list-style: none;
    font-family: "Lato", sans-serif; font-size: 19px; color: var(--ink);
  }
  .contacts li { display: flex; align-items: center; gap: 14px; margin-bottom: 14px; }
  .contacts .icon { width: 18px; height: 18px; }
  .firm-name--back {
    position: absolute; left: 60px; bottom: 70px;
    color: var(--firm-grey); font-size: 20px;
  }
</style>
</head>
<body>
<main class="canvas">
  <section class="card card--front" aria-label="Card front">
    <div class="front__panel">
      <p class="firm-name firm-name--front">Lakeshore Injury Counsel</p>
    </div>
    <div class="front__band">
      <svg class="icon" viewBox="0 0 24 24" aria-hidden="true"><path d="M12 2a7 7 0 0 0-7 7c0 5.2 7 13 7 13s7-7.8 7-13a7 7 0 0 0-7-7zm0 9.5A2.5 2.5 0 1 1 12 6.5a2.5 2.5 0 0 1 0 5z"/></svg>
      <span class="address">48 Harbor Avenue, Fairview, USA 54321</span>
    </div>
  </section>

  <section class="card card--back" aria-label="Card back">
    <div class="person">
      <div class="person__name">
        <svg class="icon" viewBox="0 0 24 24" aria-hidden="true"><circle cx="12" cy="7" r="5"/><path d="M2 23c0-6 4.5-9 10-9s10 3 10 9z"/></svg>
        <span><span class="person__first">NORA</span> <span class="person__last">BELL</span></span>
      </div>
      <p class="person__role">LAWYER</p>
    </div>
    <ul class="contacts">
      <li>
        <svg class="icon" viewBox="0 0 24 24" aria-hidden="true"><path d="M6.6 10.8a15.1 15.1 0 0 0 6.6 6.6l2.2-2.2a1 1 0 0 1 1-.25 11.4 11.4 0 0 0 3.6.57 1 1 0 0 1 1 1V20a1 1 0 0 1-1 1A17 17 0 0 1 3 4a1 1 0 0 1 1-1h3.5a1 1 0 0 1 1 1c0 1.25.2 2.45.57 3.57a1 1 0 0 1-.25 1z"/></svg>
        <span>+915-555-0147</span>
      </li>
      <li>
        <svg class="icon" viewBox="0 0 24 24" aria-hidden="true"><path d="M2 5h20v14H2zm2 2v.5l8 5 8-5V7l-8 5z"/></svg>
        <span>nora@lakeshorecounsel.com</span>
      </li>
      <li>
        <svg class="icon" viewBox="0 0 24 24" aria-hidden="true"><path d="M12 2a10 10 0 1 0 0 20 10 10 0 0 0 0-20zm6.9 9h-3a15 15 0 0 0-1.3-5.6A8 8 0 0 1 18.9 11zM12 4.1c.9 1.3 1.8 3.6 2 6.9h-4c.2-3.3 1.1-5.6 2-6.9zM9.4 5.4A15 15 0 0 0 8.1 11h-3a8 8 0 0 1 4.3-5.6zM5.1 13h3a15 15 0 0 0 1.3 5.6A8 8 0 0 1 5.1 13zm6.9 6.9c-.9-1.3-1.8-3.6-2-6.9h4c-.2 3.3-1.1 5.6-2 6.9zm2.6-1.3a15 15 0 0 0 1.3-5.6h3a8 8 0 0 1-4.3 5.6z"/></svg>
        <span>www.lakeshorecounsel.com</span>
      </li>
    </ul>
    <p class="firm-name firm-name--back">Lakeshore Injury Counsel</p>
  </section>
</main>
</body>
</html>
```